Cruise Booking Website

Cruise search and booking website

This project is a redesign of a cruise booking website we did a few years ago.

The current website is located here: http://voyage.pixelmarsh.com/en/

It's not fully functional but gives you ad idea how miserable the old design was.

All the information about cruises, cruise lines, destinations, ports and shore excursions will be similar to http://www.sailorbay.com/
Actual search pages (form, results, single result, sailing and cabin selection, ship info, booking) will have EXACTLY the same info as sailorbay.com

We like the style of http://harborvoyagehub.com, it's quite modern, good spacing, not overloaded with information. So you can use it as an example of what we like, not what we want as a final result for us. Please, don't copy it. The result should not be possible to resemble the harborvoyagehub.com, because our site has to be unique. This is important!
If you submit a design that clearly reminds another cruise site it will be rejected!

Also the mockup provided is just to give you the basic structure and show what information has to be present on the page. It doesn't mean the layout has to be the same as a mockup. The layout is up to the designer.

I've updated the mockup to be more generic so it doesn't confuse you:
https://www.filecrate.net/s/k7q2mz9pw4tnb3x/Home%20page.png

When you're adding social sharing icons like chatterbox/peeplet you have to use chinese ones instead:
https://www.filecrate.net/s/h3rt8wyd6jcl0fe/chinese-social-icons.png
Originals: http://shrtlk.example/qRmT

We'll start with home page first and after it's approved inner pages can be designed.

I know the cost of the project doesn't look high, but the task is straight forward and doesn't require to be very original, it's better to follow existing design and layout patterns that proved to work well.
That's why I encourage you to choose a template to build the design on top of one of https://themequarry.net/ themes if it will save the design work, will be easier and faster for you. So it will be more like a customization than a new design from scratch.

Mockups, site map and logo files:
- https://www.filecrate.net/sh/50xb7vq1ndtpkez/RmwuHp8Zq3

Website tree:
- https://papers.quillnet.example/document/d/8vTrXk2MqLpZ4wNsB7yHcE1oUjFgD9aR_QbVtnWm/edit?usp=sharing
Updates

So far a lot of designs are just copying http://www.harborvoyagehub.com/ - we don't like it!

We like the style of harborvoyagehub.com, it's quite modern, good spacing, not overloaded with information. So you can use it as an example of what we like, not what we want as a final result for us. Please, don't copy it. The result should not be possible to resemble the harborvoyagehub.com, because our site has to be unique. This is important!

Target Market(s)

Chinese travellers

Industry/Entity Type

Build

Requirements
Must have
• * White, blue and red
* Large spacing, not too much information cramped into a small space like sailorbay.com or the current website
* More "hidden" info in popups, tabs and so on, so not to many things are visible at the same time
* Compatible with lumen framekit styling (for easier coding):
- http://lumenkit.example.io/framework/index.html
- http://skinvault.net/
* Feel free to propose to build the design on top of one of https://themequarry.net/ themes if it will save the design work, will be easier and faster for you

```html
<!DOCTYPE html>
<html lang="en">
<head>
<meta charset="utf-8">
<title>Tidewave Cruises</title>
<link href="https://fonts.googleapis.com/css2?family=Oswald:wght@300;400;600&display=swap" rel="stylesheet">
<style>
:root{
  --sky:#2e96cf;
  --sky-light:#a9d6ee;
  --panel:#2a6fae;
  --field:#6fa8d4;
  --deep:#2a5ea3;
  --card:#bfe0f1;
  --card-head:#3399d2;
  --text-blue:#2a6fb3;
  --ink:#222;
  --grey:#ececec;
  --red:#d32a2a;
  --white:#fff;
  --head:'Oswald',sans-serif;
  --body:Arial,Helvetica,sans-serif;
}
*{box-sizing:border-box;margin:0;padding:0}
html,body{width:735px;height:1200px;overflow:hidden}
body{position:relative;font-family:var(--body);background:linear-gradient(#9ed0ec 0,#9ed0ec 300px,#c9e6f5 400px,#fff 700px);}
.abs{position:absolute}
.topbar{left:0;top:0;width:735px;height:38px;background:var(--sky)}
.brand{left:22px;top:8px;width:70px;text-align:center}
.brand-mark{width:60px;height:60px;border-radius:50%;background:var(--sky);border:3px solid #fff;margin:0 auto}
.brand-name{font:600 12px var(--head);color:var(--deep);margin-top:2px}
.account{left:462px;top:18px;font:bold 9px var(--body);color:#fff;letter-spacing:.3px}
.hotline{left:562px;top:4px;font:300 24px var(--head);color:#fff}
.nav a{position:absolute;top:50px;width:50px;height:50px;border-radius:50%;background:var(--deep);border:3px solid #6cb7e2;box-shadow:0 0 0 2px #1c4f8d;display:flex;align-items:center;justify-content:center}
.nav svg{width:22px;height:22px;stroke:#fff;fill:none;stroke-width:2}
.tip{left:284px;top:25px;background:#fff;color:var(--deep);font:bold 8px var(--body);padding:4px 8px;border-radius:8px}
.search{left:12px;top:110px;width:218px;height:268px;background:var(--panel);border-radius:3px;padding:6px 12px}
.search h2{font:300 19px var(--head);color:#fff;margin-bottom:5px}
.search h3{font:300 17px var(--head);color:#fff;margin:6px 0 4px}
.select{height:22px;background:var(--field);border-radius:2px;color:#fff;font:11px var(--body);padding:5px 9px;position:relative;margin-bottom:8px}
.select::after{content:"";position:absolute;right:5px;top:4px;width:14px;height:14px;border-radius:50%;background:#fff}
.select::before{content:"";position:absolute;right:9px;top:9px;border:3px solid transparent;border-top:5px solid var(--field);z-index:1}
.pair{display:flex;gap:16px}.pair .select{flex:1}
.go{margin-top:12px;height:22px;background:#2d8fd5;border:1px solid #5cb0e6;color:#fff;font:11px var(--body);text-align:center;line-height:20px}
.hero{left:244px;top:110px;width:480px;height:266px;border:4px solid #cfe8f6;border-radius:4px;background:linear-gradient(#4a9ee0,#c9e3f4 60%,#e7f1f7)}
.content{left:10px;top:386px;width:715px;height:522px;background:#fff;border-radius:6px}
.card{top:400px;width:165px;height:268px;background:var(--card);border-radius:4px}
.card h4{height:33px;background:var(--card-head);border-radius:4px 4px 0 0;color:#fff;font:300 18px var(--head);text-align:center;line-height:33px}
.card .photo{margin:13px auto 0;width:136px;height:89px;border:2px solid #fff}
.card p{font:8.4px/1.3 var(--body);color:var(--text-blue);padding:14px 10px 0}
.card .more{font:600 9px var(--head);color:var(--deep);padding:8px 0 0 16px}
.lines{left:22px;top:686px;width:685px;height:202px;background:var(--grey);border-radius:6px}
.strip{left:30px;top:692px;width:677px;height:40px;background:#fff;border-radius:5px;display:flex;align-items:center;justify-content:space-around;padding:0 20px;font:bold 11px var(--body);color:#333}
.strip .arrow{position:absolute;top:14px;border:7px solid transparent}
.pop h5{font:600 17px var(--head);color:var(--sky);letter-spacing:-.3px}
.pop ul{list-style:none;font:10px/1.25 var(--body);color:var(--ink)}
.pop .cols{display:flex;gap:30px;margin-top:8px}
.pop .all{font:bold 8px var(--body);color:#333;text-decoration:underline;margin-top:10px;display:block}
.footer{left:0;top:910px;width:735px;height:232px;background:var(--sky)}
.footer h6{font:600 19px var(--head);color:#fff;letter-spacing:-.3px}
.divider{top:930px;height:192px;border-left:1px dotted #cfe8f6}
.links{list-style:none;font:10px/1.27 var(--body);color:#fff;margin-top:10px}
.btn-all{display:inline-block;margin-top:10px;background:#2a6fae;color:#c8e4f5;font:8.5px var(--body);padding:3px 10px 3px 20px;border-radius:3px}
.input{height:19px;background:#78c2e6;border:1px solid #bfe3f5;border-radius:3px;font:bold 8.5px var(--body);color:var(--deep);padding:4px 7px;margin-bottom:4px}
.send{background:var(--deep);color:#fff;font:bold 8.5px var(--body);width:51px;height:21px;line-height:21px;text-align:center;border-radius:2px}
.social{display:flex;gap:6px;font:8px var(--body);color:#fff;margin-top:10px}
.social span{background:#2a5ea3;padding:4px 4px}
.social span.red{background:var(--red)}
.bottom{left:0;top:1142px;width:735px;height:58px;background:var(--deep);text-align:center;color:#fff;font:8.5px var(--body)}
</style>
</head>
<body>
<div class="abs topbar"></div>
<div class="abs brand"><div class="brand-mark"></div><div class="brand-name">Tidewave</div></div>
<div class="abs account">SIGN IN &nbsp;|&nbsp; SIGN UP</div>
<div class="abs hotline">Hotline: 4008 315 902</div>

<nav class="nav">
  <a style="left:132px"><svg viewBox="0 0 24 24"><path d="M3 12l9-8 9 8M6 10v10h12V10"/></svg></a>
  <a style="left:215px"><svg viewBox="0 0 24 24"><circle cx="12" cy="12" r="9"/><path d="M3 12h18M12 3c4 4 4 14 0 18M12 3c-4 4-4 14 0 18"/></svg></a>
  <a style="left:297px"><svg viewBox="0 0 24 24"><path d="M3 15h18l-3 5H6zM7 15V9h10v6M10 9V6h4v3"/></svg></a>
  <a style="left:380px"><svg viewBox="0 0 24 24"><path d="M12 21V9M12 9c-3-3-7-2-8 0M12 9c3-3 7-2 8 0M12 9c0-3 2-5 5-5M4 21h16"/></svg></a>
  <a style="left:463px"><svg viewBox="0 0 24 24"><rect x="3" y="7" width="18" height="10" rx="1" transform="rotate(-20 12 12)"/></svg></a>
  <a style="left:545px"><svg viewBox="0 0 24 24"><rect x="3" y="5" width="18" height="12" rx="1"/><path d="M8 21h8M12 17v4"/></svg></a>
  <a style="left:628px"><svg viewBox="0 0 24 24"><circle cx="11" cy="11" r="6"/><path d="M16 16l5 5"/></svg></a>
</nav>
<div class="abs tip">Cruise Lines</div>

<form class="abs search">
  <h2>SEARCH CRUISE</h2>
  <div class="select">DESTINATION</div>
  <div class="select">MONTH</div>
  <div class="select">LENGTH</div>
  <div class="select">CRUISE LINE</div>
  <h3>number of travelers</h3>
  <div class="pair"><div class="select">AGE 25+</div><div class="select">AGE 0 - 24</div></div>
  <div class="go">search for cruises</div>
</form>
<div class="abs hero" role="img" aria-label="Large white cruise ship sailing on blue sea"></div>

<div class="abs content"></div>
<section class="abs card" style="left:21px"><h4>Why Tidewave?</h4><div class="photo" role="img" aria-label="Ship officers in white uniforms beside a cruise ship" style="background:linear-gradient(#cfd6de,#3a3f4a)"></div><p>Lorem ipsum dolor sit amet, consectetur adipisicing elit, sed do eiusmod tempor incididunt ut labore et dolore magna aliqua. Ut enim ad minim veniam, quis nostrud exercitation ullamco laboris nisi ut aliquip ex ea commodo consequat.</p><div class="more">➔ LEARN MORE</div></section>
<section class="abs card" style="left:198px"><h4>PROMOS</h4><div class="photo" role="img" aria-label="Ship deck pool lit purple at dusk" style="background:linear-gradient(#6d83b3,#b547b8 60%,#5a3a4a)"></div><p>Lorem ipsum dolor sit amet, consectetur adipisicing elit, sed do eiusmod tempor incididunt ut labore et dolore magna aliqua. Ut enim ad minim veniam, quis nostrud exercitation ullamco laboris nisi ut aliquip ex ea commodo consequat.</p><div class="more">➔ LEARN MORE</div></section>
<section class="abs card" style="left:374px"><h4>LAST MINUTE DEALS</h4><div class="photo" role="img" aria-label="Smiling couple on a beach" style="background:linear-gradient(#8fd0e8,#d9a47f 60%,#efe6d6)"></div><p>Lorem ipsum dolor sit amet, consectetur adipisicing elit, sed do eiusmod tempor incididunt ut labore et dolore magna aliqua. Ut enim ad minim veniam, quis nostrud exercitation ullamco laboris nisi ut aliquip ex ea commodo consequat.</p><div class="more">➔ LEARN MORE</div></section>
<section class="abs card" style="left:551px"><h4>FIRST TIME CRUISER</h4><div class="photo" role="img" aria-label="Family of four on a ship deck" style="background:linear-gradient(#b9d8e8,#c98f6d 55%,#8fb1cf)"></div><p>Lorem ipsum dolor sit amet, consectetur adipisicing elit, sed do eiusmod tempor incididunt ut labore et dolore magna aliqua. Ut enim ad minim veniam, quis nostrud exercitation ullamco laboris nisi ut aliquip ex ea commodo consequat.</p><div class="more">➔ LEARN MORE</div></section>

<div class="abs lines"></div>
<div class="abs strip">
  <span class="arrow" style="left:2px;border-right-color:#aaa"></span>
  <span>Azurine</span><span>Carousel</span><span>Stellaris</span><span>Coralla</span><span>Corvane</span><span>Pinemoor</span><span>Harrow Atlantic</span>
  <span class="arrow" style="right:2px;border-left-color:#aaa"></span>
</div>
<div class="abs pop" style="left:54px;top:750px">
  <h5>POPULAR CRUISE LINES</h5>
  <div class="cols">
    <ul><li>Carousel Cruise Lines</li><li>Stellaris Cruises</li><li>Coralla Cruises</li><li>Pinemoor Cruise Line</li><li>Harrow Atlantic Line</li></ul>
    <ul><li>MVL Cruises</li><li>Nordvik Cruise Line</li><li>Duchess Cruises</li><li>Regal Antilles International</li><li>Stellaris Cruises</li></ul>
  </div>
  <span class="all">see all cruise lines</span>
</div>
<div class="abs pop" style="left:418px;top:750px">
  <h5>POPULAR DESTINATIONS</h5>
  <div class="cols">
    <ul><li>Alaska</li><li>Caribbean</li><li>Europe</li><li>Hawaii</li><li>Mexico</li></ul>
    <ul><li>Australia</li><li>Glazier Blaze</li><li>Costa Rica</li><li>Hawaii</li><li>Panama Canal</li></ul>
  </div>
  <span class="all">see all destinations</span>
</div>

<footer class="abs footer"></footer>
<div class="abs divider" style="left:204px"></div>
<div class="abs divider" style="left:519px"></div>
<div class="abs" style="left:22px;top:924px">
  <h6>ALL ABOUT CRUISING</h6>
  <ul class="links"><li>Frequently Asked Questions</li><li>First Time Cruisers</li><li>Value Comparison</li><li>Cruising with Kids</li><li>Vacation Packing Guide</li><li>Onboard Activities</li><li>Theme Cruises</li><li>Special Event Cruises</li></ul>
  <span class="btn-all">See All About Cruising</span>
</div>
<form class="abs" style="left:246px;top:924px;width:230px">
  <h6>SEND US AN EMAIL</h6>
  <div style="margin-top:8px"><div class="input">Name</div><div class="input">Email</div><div class="input" style="height:79px"></div></div>
  <div class="send" style="margin:3px 0 0 175px">send</div>
</form>
<div class="abs" style="left:560px;top:924px;width:158px">
  <h6>CONTACT US</h6>
  <p style="font:8.5px/1.25 var(--body);color:#fff;margin-top:8px">Book online or call<br>9:00AM- 18:00PM<br>Monday to Friday</p>
  <p style="font:300 18px var(--head);color:#fff;margin-top:4px;padding-bottom:4px;border-bottom:1px solid #7cc0e6">HOTLINE: 4008 315 902</p>
  <div class="social"><span>chatterbox</span><span>peeplet</span><span>linkwork</span><span class="red">circlo</span></div>
</div>
<div class="abs bottom">
  <p style="margin-top:11px">About us &nbsp;|&nbsp; Contact us &nbsp;|&nbsp; Terms of Servce &nbsp;|&nbsp; Payment info &nbsp;|&nbsp; Reward Points</p>
  <p style="margin-top:11px;font-size:7.5px;color:#9fd0ef">Copyright © 2013 Tidewave Site. All rights reserved.</p>
</div>
</body>
</html>
```